Amber Heron Fund Pitch Deck

This is a PowerPoint for use in investor presentations. The copy is written (although it may have small tweaks) and the designer will be responsible for creating a template and some graphical representations inside the presentation.

Note on the logo. Only the Amber Heron should be used, not the text.

```html
<!DOCTYPE html>
<html lang="en">
<head>
<meta charset="utf-8">
<title>Amber Heron Fund Pitch Deck</title>
<link href="https://fonts.googleapis.com/css2?family=Poppins:ital,wght@0,400;0,500;0,600;0,700;1,400;1,600&display=swap" rel="stylesheet">
<style>
:root{
  --board:#6b8cc7;
  --paper:#ffffff;
  --pale:#e8f0f9;
  --brand:#7b97cf;
  --ink:#111111;
  --grey:#7a7a7a;
  --sky:#2f9be8;
  --teal:#1a8f8a;
  --green:#6cc04a;
  --orange:#f6a43a;
}
*{margin:0;padding:0;box-sizing:border-box}
html,body{width:1200px;height:1200px;overflow:hidden;background:var(--board)}
body{font-family:'Poppins',sans-serif;color:var(--ink);position:relative}
.slide{position:absolute;width:465px;height:261px;background:var(--paper);overflow:hidden}
.s1{left:124px;top:54px}.s2{left:619px;top:54px}
.s3{left:124px;top:343px}.s4{left:619px;top:343px}
.s5{left:124px;top:631px}.s6{left:619px;top:631px}
.s7{left:124px;top:919px}
.abs{position:absolute}
.art{position:absolute;border-radius:14px}
.slide-title{font-style:italic;font-weight:600;font-size:13px;line-height:1}
.body{font-size:7px;line-height:1.15;text-align:justify}
.body p+p{margin-top:7px}

/* cover */
.cover-blob{position:absolute;left:20px;top:28px;width:420px;height:260px}
.brand-name{position:absolute;left:0;width:465px;top:82px;text-align:center;font-weight:500;font-size:23px;color:var(--brand);letter-spacing:.5px}
.brand-rule{position:absolute;left:141px;top:116px;width:188px;height:2px;background:var(--brand)}
.brand-est{position:absolute;left:0;width:465px;top:157px;text-align:center;font-size:10px;color:var(--brand);font-weight:500}
.fund-name{position:absolute;left:0;width:465px;top:210px;text-align:center;font-style:italic;font-size:17px;color:var(--grey)}

/* people */
.people{position:absolute;left:28px;top:26px;width:270px;font-size:4.6px;line-height:1.22}
.people h3{font-style:italic;font-weight:600;font-size:8.5px;line-height:1}
.people h4{font-weight:600;font-size:5px;margin-top:4px}
.people h4:first-of-type{margin-top:0}
.people li{list-style:none;padding-left:3px;text-indent:-3px}
.people li::before{content:"• "}

/* market */
.market{position:absolute;left:24px;top:18px;width:255px;font-size:4.4px;line-height:1.2}
.market h3{font-style:italic;font-weight:600;font-size:8px;margin-bottom:6px}
.market p{margin-bottom:5px}
.market li{list-style:none}
.market li::before{content:"• "}
.chart-title{position:absolute;left:24px;top:156px;font-style:italic;font-weight:600;font-size:6px}
.chart{position:absolute;left:24px;top:165px}
.ring{position:absolute;width:84px;height:84px}
.ring-year{position:absolute;left:0;width:84px;top:29px;text-align:center;font-weight:600;font-size:15px}
.ring-value{position:absolute;width:120px;text-align:center;font-weight:600;font-size:9.5px;color:var(--sky)}

/* structure */
.col{position:absolute;top:164px;width:76px;font-size:3.6px;line-height:1.5}
.col h5{font-style:italic;font-weight:600;font-size:4.6px;line-height:1.15;margin-bottom:6px}
.col p+p{margin-top:4px}

.thanks{position:absolute;left:0;width:465px;top:116px;text-align:center;font-weight:700;font-size:39px;letter-spacing:-.5px}
</style>
</head>
<body>

<section class="slide s1">
  <svg class="cover-blob" viewBox="0 0 420 260" aria-hidden="true"><path d="M110 40 C140 -10 250 0 300 60 C360 80 420 140 400 200 C390 240 360 260 330 260 L40 260 C-10 230 0 160 60 140 C90 120 80 80 110 40Z" fill="var(--pale)"/></svg>
  <div class="brand-name">The Coral Office</div>
  <div class="brand-rule"></div>
  <div class="brand-est">Est. 2022</div>
  <div class="fund-name">Amber Heron NPL Fund</div>
</section>

<section class="slide s2">
  <div class="art" style="left:19px;top:52px;width:218px;height:150px;background:linear-gradient(135deg,#dfe9f8,#f7c97a 60%,#f28a4a)" role="img" aria-label="Illustration of a team beside a rising bar chart with coins and an upward arrow"></div>
  <div class="abs" style="left:247px;top:103px;width:199px">
    <div class="slide-title" style="margin-bottom:8px">The Edge</div>
    <div class="body">
      <p>Experience with fund management and asset disposal. Utilizing the clues and hints that borrowers and guarantors leave on the Internet, we can special service assets and collect on them more quickly and maximize return.</p>
      <p>Much of the technology and experience as a team can be attributed to the team’s experience at Oakseed. The principals were the management team that came on in March 2020 and grew the business from less than 12,000 PPP loans to more than 800,000.</p>
    </div>
  </div>
</section>

<section class="slide s3">
  <div class="art" style="left:20px;top:80px;width:225px;height:122px;background:linear-gradient(135deg,#3d8fe0,#f7b531 65%,#f08b2c)" role="img" aria-label="Illustration of a businessman beside stacked coins and a rising arrow"></div>
  <div class="abs" style="left:246px;top:104px;width:199px">
    <div class="slide-title" style="margin-bottom:8px">The Technology</div>
    <div class="body">
      <p>Most lenders and servicers use LendCore or ServiLoan and then software like CollectPro for collections.</p>
      <p>These software packages fail to address the most important factors which is to analyze the borrower (and the guarantors) to allow for customized collection plans. We use enhanced skip tracing developed during PPP forgiveness and collection efforts with advanced social media logic.</p>
      <p>Finally, we use evolving algorithms to price and purchase NPL portfolios at the correct price.</p>
    </div>
  </div>
</section>

<section class="slide s4">
  <div class="people">
    <h3>The People</h3>
    <h4>Grant Holloway, Managing Partner, Investment Committee</h4>
    <ul><li>More than 20 years of banking experience with Stanhope Securities, Union Federal Bank and Ninefold Bank</li>
    <li>Director of Redfield Capital Management, in less than 5 years, achieved 4x AUM and outsized returns managing distressed asset fund. Developed framework for additional funds.</li>
    <li>CEO of Oakseed.</li></ul>
    <h4>Nathan Ferrell, Managing Partner, Investment Committee</h4>
    <ul><li>Founder of Meridian Law in Scottsdale, Arizona which became the first law firm in the country sold to private non-lawyer investors.</li>
    <li>Extensive experience with large transactions (including leading the largest 2017 Arizona transaction on behalf of a client). Known for liquidation sales inside bankruptcy. Speaker at National Insolvency Institute conference in Las Vegas.</li>
    <li>COO of Webforge, an early web development company that first implemented a commercially successful e-commerce campaign.</li>
    <li>General Counsel of Oakseed.</li></ul>
    <h4>Owen Maddox, Investment Committee</h4>
    <ul><li>CEO of Waypoint Impact Corp. (OTCQB: WYPT)</li><li>CEO, CircuitBank</li><li>Director, FirstLane Bank</li>
    <li>Member, Hispanic Board Leaders Association</li>
    <li>Peter Lindqvist, Director of Credit Analytics. Product and data specialist with more than 15 years technology and startup experience.</li>
    <li>Founded Chatterly Communications, which combined email and chat for customer success professionals. Raised $5 million capital and had more than 40,000 users.</li>
    <li>Led advertising products at Toolbench and grew from $7 million to $45 million in revenue over 5 years.</li>
    <li>Advisory Board member with well-known venture capital firm.</li><li>VP, Products, Oakseed.</li></ul>
    <h4>Lucas Brenner, Chief Operating Officer</h4>
    <ul><li>Management Consultant at Ashford &amp; Company and LRTW</li><li>Founder of two companies that grew to more than 1,000 employees.</li><li>COO of Oakseed.</li></ul>
  </div>
  <div class="art" style="left:300px;top:62px;width:156px;height:140px;background:linear-gradient(135deg,#dce7f6,#6cc04a 55%,#2c3f73)" role="img" aria-label="Illustration of a team celebrating around a desk with a laptop"></div>
</section>

<section class="slide s5">
  <div class="market">
    <h3>The Market</h3>
    <p>The commercial lending market size was valued at $8,823.53 billion in 2020, and is projected to reach $29,379.83 billion by 2030, growing at a CAGR of 13.1% from 2021 to 2030.</p>
    <p>The credit cycle is entering into a period of rising interest rates and corresponding defaults. The fund seeks to take advantage of that emerging opportunity.</p>
    <p>Our Process</p>
    <ul style="margin-bottom:5px"><li>Work with our lender customers on their non-performing loan portfolio.</li><li>Purchase participation in non-performing loans.</li><li>Provide special servicing in compliance with bank’s servicing criteria.</li><li>Provide bank access to NPL platform.</li><li>Maintain first right of refusal to purchase loan using proprietary algorithm.</li><li>Internal servicing standards.</li><li>Liquidation, when necessary.</li></ul>
    <p>Initially partner with licensed collection agencies to supplement our in-house abilities (and comply with regulatory requirements). Potential to acquire and bring completely in-house.</p>
  </div>
  <div class="chart-title">Commercial Lending Market</div>
  <svg class="chart" width="224" height="92" viewBox="0 0 224 92" aria-label="Line chart of commercial lending market, 2020 and 2030">
    <g stroke="#eeeeee" stroke-width=".5">
      <line x1="10" y1="8" x2="220" y2="8"/><line x1="10" y1="15" x2="220" y2="15"/><line x1="10" y1="22" x2="220" y2="22"/><line x1="10" y1="29" x2="220" y2="29"/><line x1="10" y1="36" x2="220" y2="36"/><line x1="10" y1="43" x2="220" y2="43"/><line x1="10" y1="50" x2="220" y2="50"/><line x1="10" y1="57" x2="220" y2="57"/><line x1="10" y1="64" x2="220" y2="64"/><line x1="10" y1="71" x2="220" y2="71"/><line x1="10" y1="78" x2="220" y2="78"/>
    </g>
    <g font-size="2.4" fill="#888" font-family="Poppins,sans-serif">
      <text x="7" y="79" text-anchor="end">0</text><text x="7" y="44" text-anchor="end">50</text><text x="7" y="9" text-anchor="end">100</text>
      <text x="15" y="86">JAN</text><text x="32" y="86">FEB</text><text x="49" y="86">MAR</text><text x="66" y="86">APR</text><text x="83" y="86">MAY</text><text x="100" y="86">JUN</text><text x="117" y="86">JUL</text><text x="134" y="86">AUG</text><text x="151" y="86">SEP</text><text x="168" y="86">OCT</text><text x="185" y="86">NOV</text><text x="202" y="86">DEC</text>
    </g>
    <circle cx="178" cy="6" r="1.2" fill="var(--sky)"/><text x="180" y="7" font-size="2.6" fill="#555" font-family="Poppins,sans-serif">2020</text>
    <circle cx="193" cy="6" r="1.2" fill="var(--green)"/><text x="195" y="7" font-size="2.6" fill="#555" font-family="Poppins,sans-serif">2030</text>
    <polyline fill="none" stroke="var(--green)" stroke-width=".8" points="12,50 30,43 48,50 66,29 84,29 102,36 120,29 138,29 156,19.5 174,15 192,19.5 210,15"/>
    <polyline fill="none" stroke="var(--sky)" stroke-width=".8" points="12,71 30,57 48,64 66,43 84,36 102,50 120,43 138,50 156,36 174,22 192,36 210,22"/>
    <g fill="var(--green)"><circle cx="12" cy="50" r=".9"/><circle cx="30" cy="43" r=".9"/><circle cx="48" cy="50" r=".9"/><circle cx="66" cy="29" r=".9"/><circle cx="84" cy="29" r=".9"/><circle cx="102" cy="36" r=".9"/><circle cx="120" cy="29" r=".9"/><circle cx="138" cy="29" r=".9"/><circle cx="156" cy="19.5" r=".9"/><circle cx="174" cy="15" r=".9"/><circle cx="192" cy="19.5" r=".9"/><circle cx="210" cy="15" r=".9"/></g>
    <g fill="var(--sky)"><circle cx="12" cy="71" r=".9"/><circle cx="30" cy="57" r=".9"/><circle cx="48" cy="64" r=".9"/><circle cx="66" cy="43" r=".9"/><circle cx="84" cy="36" r=".9"/><circle cx="102" cy="50" r=".9"/><circle cx="120" cy="43" r=".9"/><circle cx="138" cy="50" r=".9"/><circle cx="156" cy="36" r=".9"/><circle cx="174" cy="22" r=".9"/><circle cx="192" cy="36" r=".9"/><circle cx="210" cy="22" r=".9"/></g>
  </svg>

  <div class="ring" style="left:327px;top:32px">
    <svg width="84" height="84" viewBox="0 0 84 84" aria-hidden="true">
      <circle cx="42" cy="42" r="35" fill="none" stroke="#cfcfcf" stroke-width="7" stroke-dasharray="0.9 1.3"/>
      <circle cx="42" cy="42" r="35" fill="none" stroke="var(--sky)" stroke-width="7" stroke-dasharray="0.9 1.3" pathLength="220" transform="rotate(-90 42 42)" style="stroke-dasharray:0.9 1.3;" clip-path="url(#c20)"/>
      <clipPath id="c20"><path d="M42 42 L42 0 L76 0 L84 28Z"/></clipPath>
    </svg>
    <div class="ring-year">2020</div>
  </div>
  <div class="ring-value" style="left:309px;top:119px">$8,823.53 billion</div>

  <div class="ring" style="left:329px;top:138px">
    <svg width="84" height="84" viewBox="0 0 84 84" aria-hidden="true">
      <circle cx="42" cy="42" r="35" fill="none" stroke="#cfcfcf" stroke-width="7" stroke-dasharray="0.9 1.3"/>
      <circle cx="42" cy="42" r="35" fill="none" stroke="var(--teal)" stroke-width="7" stroke-dasharray="0.9 1.3" clip-path="url(#c30)"/>
      <clipPath id="c30"><path d="M42 42 L42 0 L84 0 L84 84 L70 84Z"/></clipPath>
    </svg>
    <div class="ring-year">2030</div>
  </div>
  <div class="ring-value" style="left:309px;top:225px">$29,379.83 billion</div>
</section>

<section class="slide s6">
  <div class="art" style="left:22px;top:48px;width:76px;height:110px;background:linear-gradient(160deg,#4b52d8,#f27a6a)" role="img" aria-label="Illustration of a woman with a laptop and customer avatars"></div>
  <div class="art" style="left:108px;top:48px;width:76px;height:110px;background:linear-gradient(160deg,#f06a4a,#f5cc6e)" role="img" aria-label="Illustration of a person with a flag atop a rising arrow"></div>
  <div class="art" style="left:195px;top:48px;width:76px;height:110px;background:linear-gradient(160deg,#f6c94a,#2c3f73)" role="img" aria-label="Illustration of a manager at a laptop with an idea bulb"></div>
  <div class="art" style="left:282px;top:48px;width:76px;height:110px;background:linear-gradient(160deg,#f4a0a0,#f06a5a)" role="img" aria-label="Illustration of a light bulb with coins and network icons"></div>
  <div class="art" style="left:369px;top:48px;width:76px;height:110px;background:linear-gradient(160deg,#4fa3f0,#1e5fc8)" role="img" aria-label="Illustration of a person with a laptop on a stack of coins"></div>

  <div class="col" style="left:22px"><h5>Our Customers</h5><p>Target market: banks that hold special assets. We source from trusted relationships and explain why we have a leg up on pipeline.</p><p>Community banks: Nearly 5,000<br>Mid-Market banks: Approximately 4,000</p></div>
  <div class="col" style="left:108px"><h5>Advantage</h5><p>Tech plus capital: a high tech approach to understanding credit performance and verification of circumstances. Capital as a percentage of total and co-investment against first round of raise.</p></div>
  <div class="col" style="left:195px"><h5>Management Structure</h5><p>AHRN Management, LLC to provide management. The same people as above or just eliminate reference.</p><p>Three partners to serve on Investment Committee</p></div>
  <div class="col" style="left:282px"><h5>Waypoint Co-Sponsored Fund</h5><p>Utilize Waypoint network, AHRN technology. Joint LP investment, Waypoint affiliates and partners provide additional LP investment.</p><p>NPL fund LLC to be GP, 80% of carry to AHRN and 20% to Waypoint.</p></div>
  <div class="col" style="left:369px"><h5>Projected Size of Fund – Initially $200 million, up to $1 billion</h5><p>$100 million commitment from AHRN from funds due from CPF.</p><p>$100 million commitment from Waypoint or its affiliates.</p></div>
</section>

<section class="slide s7">
  <div class="thanks">Thank You</div>
</section>

</body>
</html>
```